Cocktail Menu

I need a drink menu that will be prited on a heavy weight card designed. I want it to be something differtent that guests will look at then order a drink. The card will be on the bar or given to customers at tables. This is for a upscale restaurant in Northern Virginia. The website is www.BriarmossRestaruant.com if you want to see pictures. I will attach rthe drinks and our logo. I need something really attractive and different. It can be larger then a postcard but not stanadard paper sizes.
Updates

The menu can be larger then a postcard and the front and back can be used if needed.

Industry/Entity Type

Restaurant

```html
<!DOCTYPE html>
<html lang="en">
<head>
<meta charset="utf-8">
<title>Briarmoss Restaurant – Cocktail Menu</title>
<link href="https://fonts.googleapis.com/css2?family=Fondamento:ital@0;1&family=Open+Sans:ital,wght@0,600;1,700&display=swap" rel="stylesheet">
<style>
  :root {
    --page-bg: #ffffff;
    --card-bg: #ffffff;
    --ink: #2a3590;
    --logo-ink: #1a1a1a;
    --blue: #6cc4ea;
    --green: #8cc63f;
    --yellow: #f6e33a;
    --orange: #f7941d;
    --red: #ee3a2b;
    --magenta: #c9418f;
  }
  * { margin: 0; padding: 0; box-sizing: border-box; }
  html, body { width: 1200px; height: 1000px; overflow: hidden; background: var(--page-bg); }
  .menu-card {
    position: absolute; left: 422px; top: 38px; width: 355px; height: 924px;
    background: var(--card-bg); overflow: hidden;
    box-shadow: 0 0 3px rgba(0,0,0,0.12);
  }
  .color-wash {
    position: absolute; left: 10px; right: 0; top: 40px; bottom: 0;
    background: linear-gradient(to right,
      rgba(108,196,234,0.05) 0%, rgba(108,196,234,0.55) 14%,
      rgba(140,198,63,0.6) 28%, rgba(246,227,58,0.6) 42%,
      rgba(247,148,29,0.6) 58%, rgba(238,58,43,0.7) 76%,
      rgba(247,148,29,0.45) 86%, rgba(201,65,143,0.75) 100%);
    -webkit-mask-image: linear-gradient(to bottom, transparent 0%, rgba(0,0,0,0.35) 25%, rgba(0,0,0,0.8) 70%, #000 100%);
    mask-image: linear-gradient(to bottom, transparent 0%, rgba(0,0,0,0.35) 25%, rgba(0,0,0,0.8) 70%, #000 100%);
  }
  .brand { position: absolute; left: 0; right: 0; top: 132px; text-align: center; color: var(--logo-ink); }
  .brand-name { font-family: 'Open Sans', sans-serif; font-weight: 600; font-size: 30px; letter-spacing: 1px; line-height: 34px; }
  .brand-rule { width: 186px; height: 2px; margin: 2px auto 4px; background: var(--logo-ink); }
  .brand-tag { font-family: 'Open Sans', sans-serif; font-weight: 600; font-size: 12px; letter-spacing: 4px; line-height: 16px; }
  .section-title, .drink-name {
    position: relative; font-family: 'Fondamento', cursive; font-style: italic; color: var(--ink); font-weight: 400;
  }
  .section-title { position: absolute; left: 30px; font-size: 24px; line-height: 26px; }
  .drink { position: absolute; left: 30px; width: 292px; }
  .drink-name { font-size: 16px; line-height: 20px; }
  .drink-desc {
    position: relative; font-family: 'Open Sans', sans-serif; font-style: italic; font-weight: 700;
    font-size: 11.5px; line-height: 15px; color: var(--ink); width: 250px;
  }
  .price {
    position: absolute; right: 0; bottom: 0; font-family: 'Open Sans', sans-serif; font-style: italic;
    font-weight: 700; font-size: 14px; line-height: 15px; color: var(--ink);
  }
</style>
</head>
<body>
  <main class="menu-card">
    <div class="color-wash" role="img" aria-label="Vertical rainbow stripes with soft bokeh light circles"></div>

    <header class="brand">
      <div class="brand-name">BRIARMOSS</div>
      <div class="brand-rule"></div>
      <div class="brand-tag">RESTAURANT</div>
    </header>

    <div class="drink" style="top:206px">
      <h3 class="drink-name">Southern Manhattan</h3>
      <p class="drink-desc">Smooth Millers Mill Whiskey, Sweet Vermouth, Bourbon Cherries</p>
      <span class="price">$12</span>
    </div>

    <h2 class="section-title" style="top:276px">Martinis</h2>

    <div class="drink" style="top:310px">
      <h3 class="drink-name">The Old Banker</h3>
      <p class="drink-desc">Iced Cold Tobin's Handmade Vodka, Blue Cheese Olives</p>
      <span class="price">$12</span>
    </div>
    <div class="drink" style="top:366px">
      <h3 class="drink-name">French Kiss Martini</h3>
      <p class="drink-desc">Starov Raspberry, Chalmont, Pineapple</p>
      <span class="price">$10</span>
    </div>
    <div class="drink" style="top:408px">
      <h3 class="drink-name">Honey Apple Nip Martini</h3>
      <p class="drink-desc">Honey Jake Donnelly, Gander Vodka, Cider, Fall Spices and touch of Honey</p>
      <span class="price">$11</span>
    </div>
    <div class="drink" style="top:465px">
      <h3 class="drink-name">Italiano Lemon Drop</h3>
      <p class="drink-desc">Starov Citrus Vodka, Lemoncello, Crystallized Rim, Lemon Twist</p>
      <span class="price">$11</span>
    </div>
    <div class="drink" style="top:521px">
      <h3 class="drink-name">Cheng Jiang Martini</h3>
      <p class="drink-desc">Barcosa O, Canter Ginger, Tuvella, OJ</p>
      <span class="price">$11</span>
    </div>
    <div class="drink" style="top:562px">
      <h3 class="drink-name">Perfect Pear</h3>
      <p class="drink-desc">Absolen Pear Vodka, St. Gervais, Peach Schnapps, Apple Juice</p>
      <span class="price">$10</span>
    </div>

    <h2 class="section-title" style="top:633px">Cocktails</h2>

    <div class="drink" style="top:667px">
      <h3 class="drink-name">The Tipsy Judge</h3>
      <p class="drink-desc">Prosecco, St. Gervais, Gin, and Japanese Yuzu, and a Strawberry</p>
      <span class="price">$12</span>
    </div>
    <div class="drink" style="top:723px">
      <h3 class="drink-name">Tart Love</h3>
      <p class="drink-desc">Bramley Gin, Camporo, St. Gervaise, Pineapple</p>
      <span class="price">$10</span>
    </div>
    <div class="drink" style="top:779px">
      <h3 class="drink-name">I Love Lola</h3>
      <p class="drink-desc">Starov Vanilla, Chalmont, Pineapple Juice, Champagne</p>
      <span class="price">$10</span>
    </div>
    <div class="drink" style="top:836px">
      <h3 class="drink-name">Brazilian Fresh</h3>
      <p class="drink-desc">12 Reed Rum, Fresh Lime, and Grapefruit</p>
      <span class="price">$12</span>
    </div>
  </main>
</body>
</html>
```